当案件にご興味をもっていただき、誠にありがとうございます。 私は、オーダースーツ白鳳堂の3代目社長の三浦と申します。 ・創業80年、オーダースーツ店おすすめランンキング1位 ・https://hakuhodo-suits.example.jp/ この度、既に撮影済みのYoutube動画のサムネイル作成を、 公募(採用確約)させていただくことにいたしました。 【動画掲載の目的】 採用ページに掲載し、「社長(三浦)が怖くはないよ!」と伝えること。 「老舗企業の社長」というだけで、少し怖いイメージがあるようです。 【動画本編】 https://video.example.com/w/Qz3kTm8LpVa 【動画掲載場所】 https://hakuhodo-suits.example.jp/company/recruit/ (このページに馴染むデザインを希望) デザイン参考、構成案、画像素材は、添付ファイルの通りです。 【YouTubeサムネイルのサイズ】 1280×720ピクセル 【最大ファイルサイズ】 2 MB 【ファイル形式】 png 【採用確約】 ご提案いただいた中から、必ず選ばせていただきます。 選出後に、多少の修正をお願いする可能性はございます。 その他ご質問等ありましたら、気軽にいただけましたら幸いです。 皆様からのご応募をお待ちしております! |
採用の理由
とても爽やかで、素敵なサムネイルをありがとうございました!
学生さんから見た時も、親しみやすく、クリックがしやすい印象だと感じ、採用させていただきました。
また、ご依頼した文字数がとても多かったのですが、分かりやすく配置していただけて、大変ありがたく感じております。また機会がございましたら、どうぞよろしくお願いいたします。
応募者全員へのお礼・コメント
この度は、ご提案を誠にありがとうございました。
様々に工夫をしていただき、素敵なサムネイルを作成していただけましたこと、大変ありがたく感じております。
また別の機会もあるかと思いますので、その際には、ご縁をいただけますと幸いです。
改めて、多くのコンペの中から弊社の公募を見つけ、ご応募くださり、誠にありがとうございました。

```html
<!DOCTYPE html>
<html lang="ja">
<head>
<meta charset="utf-8">
<title>失敗しないリクルートスーツの選び方 6つのポイント</title>
<link rel="stylesheet" href="https://fonts.googleapis.com/css2?family=Shippori+Mincho+B1:wght@700;800&display=swap">
<style>
  :root {
    --panel-blue: rgba(22, 58, 170, 0.9);
    --band-navy: #13307f;
    --title-gold: #f2c94c;
    --text-white: #ffffff;
    --text-ink: #1c2340;
    --bubble-white: #ffffff;
    --photo-light: #eef1ea;
    --photo-green: #a9bf8a;
    --photo-suit: #1d2748;
  }
  html, body {
    margin: 0;
    padding: 0;
    width: 1200px;
    height: 670px;
    overflow: hidden;
    background: #fff;
  }
  .thumbnail {
    position: relative;
    width: 1200px;
    height: 670px;
    overflow: hidden;
    font-family: "Shippori Mincho B1", serif;
    font-weight: 800;
  }
  .portrait-photo {
    position: absolute;
    inset: 0;
    background:
      radial-gradient(ellipse 230px 330px at 770px 520px, var(--photo-suit) 0%, var(--photo-suit) 70%, transparent 72%),
      linear-gradient(100deg, var(--photo-light) 0%, #f7f8f4 35%, #d9e3c9 60%, var(--photo-green) 85%, #c7d4b1 100%);
  }
  .lead-panel {
    position: absolute;
    left: 16px;
    top: 64px;
    width: 580px;
    height: 132px;
    background: var(--panel-blue);
    color: var(--text-white);
    font-size: 31px;
    line-height: 50px;
    padding: 16px 0 0 24px;
    box-sizing: border-box;
    letter-spacing: 0.02em;
  }
  .lead-panel p { margin: 0; }
  .speech-bubble {
    position: absolute;
    left: 790px;
    top: 140px;
    width: 260px;
    height: 140px;
  }
  .speech-bubble svg { position: absolute; inset: 0; }
  .speech-bubble .bubble-text {
    position: absolute;
    left: 0;
    right: 0;
    top: 30px;
    text-align: center;
    color: var(--text-ink);
    font-size: 22px;
    line-height: 36px;
  }
  .title-panel {
    position: absolute;
    left: 0;
    top: 330px;
    width: 860px;
    height: 196px;
    background: var(--panel-blue);
    color: var(--title-gold);
    font-size: 46px;
    line-height: 70px;
    padding: 28px 0 0 20px;
    box-sizing: border-box;
  }
  .title-panel p { margin: 0; }
  .title-panel .second-line { padding-left: 18px; }
  .credit-band {
    position: absolute;
    left: 0;
    top: 572px;
    width: 1190px;
    height: 52px;
    background: var(--band-navy);
    color: var(--text-white);
    font-size: 21px;
    line-height: 52px;
    padding-left: 20px;
    box-sizing: border-box;
    white-space: nowrap;
    letter-spacing: -0.01em;
  }
</style>
</head>
<body>
  <main class="thumbnail">
    <div class="portrait-photo" role="img" aria-label="オフィスの窓辺で笑顔を見せるネイビーのスーツ姿の社長の写真"></div>

    <div class="lead-panel">
      <p>創業８０年超えのオーダースーツ店</p>
      <p>銀座白鳳堂の社長が語る</p>
    </div>

    <div class="speech-bubble">
      <svg width="260" height="140" viewBox="0 0 260 140" aria-hidden="true">
        <ellipse cx="130" cy="66" rx="126" ry="60" fill="var(--bubble-white)"/>
        <path d="M40 104 L18 138 L70 116 Z" fill="var(--bubble-white)"/>
      </svg>
      <div class="bubble-text">就活生が<br>今すぐ取り入れられる！</div>
    </div>

    <div class="title-panel">
      <p>「失敗しないリクルートスーツの選び方</p>
      <p class="second-line">６つのポイント」</p>
    </div>

    <div class="credit-band">オーダースーツ店おすすめランキング１位！ドラマ「高坂直人」、森川拓海さん主演「誠実不動産」、藤咲由衣さんご着用</div>
  </main>
</body>
</html>
```